BRIGHTDESK - Remote Tech Support Site

We are looking for a new very responsive and simple website for our brand Brightdesk.com - a remote technical support company.

This company supports customers Globally in different countries throughout Eur/ North America / South America / Asia etc (please keep this in mind and integrate into the idea).

Its important to us that the design is very explanatory, the customer should easily be able to figure out that we provide computer support right away ... I like one page responsive type designs as well without a bunch of menu items

Here are some similar sites we like - but still looking for a unique design that fits out brand "brightdesk" - I have upload also some layouts i like (but the designs are not important just the layouts), youll see it includes consumer business etc which is important.

VOLM.COM - I love how clean it is - nice and white easy to see everything

PLUMWIRE247.COM - also nice the layout and responsive one page design makes it easy to use

corvalfix.com - similar to plumwire design as well - you can get the idea im looking for between the two

You will notice those examples are much different then the attachments I added - again this is more of an idea for possible layouts .. attached is also the logo - could inspire color scheme / blue white black etc

Target Market(s)

Home consumers without computer knowledge , older age 45-65, small medium business ... computer repair - slow computers

Industry/Entity Type

Computer Repair

Logo Text

Brightdesk

Coding

Coded - Design and coding required

Number of Pages Required

1 page

Font styles to use
Sans Serif
Other font styles liked:
• your choice responsive

Colors

Designer to choose colors to be used in the design.

Requirements
Must have
• Clean - responsive - professional design - the name says it all - brightdesk
• CALL TO ACTIONS FOR "Get Help Now!" / "Learn More" etc
Nice to have
• We are looking for a new very responsive and simple website for our brand Brightdesk.com - a remote technical support company.
• This company supports customers Globally in different countries throughout Eur/ North America / South America / Asia etc (please keep this in mind and integrate into the idea).
• Its important to us that the design is very explanatory, the customer should easily be able to figure out that we provide computer support right away ... I like one page responsive type designs as well without a bunch of menu items
• Here are some similar sites we like - but still looking for a unique design that fits out brand "brightdesk" - I have upload also some layouts i like (but the designs are not important just the layouts), youll see it includes consumer business etc which is important.
• VOLM.COM - I love how clean it is - nice and white easy to see everything
• PLUMWIRE247.COM - also nice the layout and responsive one page design makes it easy to use
• corvalfix.com - similar to plumwire design as well - you can get the idea im looking for between the two
Should not have
• dark, packed page - bad small font -

```html
<!DOCTYPE html>
<html lang="en">
<head>
<meta charset="utf-8">
<title>Brightdesk – Remote Tech Support</title>
<link href="https://fonts.googleapis.com/css2?family=Roboto:wght@300;400;500;700;900&display=swap" rel="stylesheet">
<style>
:root{
  --blue:#1e90ec;
  --blue-dark:#1577c9;
  --green:#5aa634;
  --green-dark:#4a8d29;
  --ink:#2a2f35;
  --text:#555b62;
  --muted:#8a9097;
  --light:#f2f4f6;
  --grey:#e9ebed;
  --footer:#2a2c2f;
  --footer-text:#9a9ea3;
  --white:#ffffff;
}
*{margin:0;padding:0;box-sizing:border-box}
html,body{width:1200px;height:4167px;overflow:hidden}
body{font-family:'Roboto',Arial,sans-serif;color:var(--text);background:var(--white);position:relative}
.abs{position:absolute}
.btn{position:absolute;display:flex;align-items:center;justify-content:center;font-weight:500;text-transform:uppercase;letter-spacing:.5px;border-radius:2px}
.photo{position:absolute}

/* top */
.hero{position:absolute;left:0;top:0;width:1200px;height:617px;background:linear-gradient(90deg,#f5f7f9 0%,#eef1f4 45%,#e3e7eb 100%)}
.hero-photo{left:520px;top:0;width:680px;height:617px;background:linear-gradient(120deg,#eef1f4 0%,#d9dfe5 35%,#c9b9a6 60%,#dfe3e7 100%)}
.topbar{position:absolute;left:0;top:0;width:1200px;height:24px;background:rgba(40,46,52,.55);color:#fff;font-size:11px}
.topbar .email{left:161px;top:5px}
.topbar .right{left:940px;top:5px;display:flex;gap:18px}
.nav{position:absolute;left:0;top:24px;width:1200px;height:60px;background:rgba(60,66,72,.35)}
.logo{position:absolute;display:flex;align-items:center;gap:8px;font-weight:700;font-size:30px;color:#fff;letter-spacing:-.5px}
.logo .dot{width:34px;height:34px;border-radius:50%;background:var(--blue)}
.nav .logo{left:161px;top:12px}
.nav-links{position:absolute;left:500px;top:22px;display:flex;gap:22px;font-size:12px;font-weight:700;color:#fff}
.nav-phone{position:absolute;left:883px;top:17px;display:flex;align-items:center;gap:8px;color:#fff;font-size:22px;font-weight:700}
.hero h1{position:absolute;left:161px;top:160px;font-size:44px;font-weight:700;color:var(--blue);line-height:1}
.hero h2{position:absolute;left:161px;top:208px;font-size:44px;font-weight:300;color:var(--ink);line-height:1}
.hero-list{position:absolute;left:161px;top:282px;display:grid;grid-template-columns:200px 200px;row-gap:14px;font-size:12px;color:var(--ink)}
.hero-list li{list-style:none;display:flex;align-items:center;gap:8px}
.hero-list li:before{content:"";width:6px;height:6px;border-radius:50%;background:var(--muted)}
.hero-list b{color:var(--blue);font-weight:500}
.hero .cta{left:161px;top:379px;width:166px;height:38px;background:var(--blue);color:#fff;font-size:13px;text-transform:none;letter-spacing:0;font-weight:400}

/* member bar */
.member{position:absolute;left:161px;top:575px;width:875px;height:86px;background:#fff;box-shadow:0 3px 12px rgba(0,0,0,.12);z-index:2}
.member .icon{position:absolute;left:0;top:0;width:183px;height:86px;background:var(--green);display:flex;align-items:center;justify-content:center}
.member h3{position:absolute;left:203px;top:20px;font-size:24px;font-weight:700;color:var(--ink)}
.member p{position:absolute;left:203px;top:52px;font-size:11px;color:var(--text)}
.member .go{left:728px;top:22px;width:125px;height:40px;background:var(--green);color:#fff;font-size:13px;font-weight:700;gap:8px}

/* how it works */
.how{position:absolute;left:0;top:617px;width:1200px;height:494px;background:linear-gradient(#f7f8f9,#eceff1)}
.sec-title{position:absolute;left:0;width:1200px;text-align:center;font-weight:700;color:var(--ink)}
.how .sec-title{top:88px;font-size:30px}
.how .lead{position:absolute;left:200px;top:136px;width:800px;text-align:center;font-size:12px;line-height:1.6}
.step{position:absolute;top:200px;width:270px;text-align:center}
.step .ring{width:88px;height:88px;margin:0 auto;border-radius:50%;border:3px solid var(--blue);background:#fff;display:flex;align-items:center;justify-content:center}
.step h4{margin-top:18px;font-size:16px;font-weight:500;color:var(--ink)}
.step p{margin-top:10px;font-size:11px;line-height:1.55}
.how .more{left:532px;top:424px;width:136px;height:38px;border:2px solid var(--ink);color:var(--ink);font-size:12px;gap:8px}

/* blue band */
.band{position:absolute;left:0;top:1111px;width:1200px;height:178px;background:var(--blue);color:#fff;text-align:center}
.band h3{margin-top:36px;font-size:32px;font-weight:500}
.band p{margin-top:8px;font-size:17px;font-weight:300}
.band .contact{left:533px;top:114px;width:128px;height:36px;background:#fff;color:var(--blue);font-size:13px}

/* products */
.products{position:absolute;left:0;top:1289px;width:1200px;height:503px;background:linear-gradient(#f0f2f4,#f8f9fa)}
.products .sec-title{top:32px;font-size:32px;font-weight:500}
.product{position:absolute;top:108px;width:203px;text-align:center}
.product .shot{width:203px;height:242px;border:4px solid #fff;box-shadow:0 2px 8px rgba(0,0,0,.2)}
.product .cap{margin-top:10px;font-size:13px;color:var(--ink)}
.product .price{margin-top:6px;font-size:21px;font-weight:700;color:var(--ink)}
.product .row{display:flex;justify-content:space-between;margin-top:12px}
.product .row span{width:88px;height:26px;display:flex;align-items:center;justify-content:center;font-size:11px;color:#fff;border-radius:2px}
.view{background:var(--green)}
.cart{background:var(--blue)}

/* real-time */
.realtime{position:absolute;left:0;top:1792px;width:1200px;height:472px;background:var(--light)}
.family{left:0;top:0;width:597px;height:472px;background:linear-gradient(135deg,#d8cbbd 0%,#c29a80 40%,#e6e1dc 100%)}
.realtime .t1{position:absolute;left:639px;top:52px;font-size:44px;font-weight:700;color:var(--ink);line-height:1}
.realtime .t2{position:absolute;left:639px;top:100px;font-size:35px;font-weight:300;color:var(--ink);line-height:1}
.realtime .t3{position:absolute;left:639px;top:138px;font-size:44px;font-weight:700;color:var(--green);line-height:1}
.ticks{position:absolute;left:639px;top:210px;list-style:none;font-size:13px;color:var(--ink)}
.ticks li{display:flex;align-items:center;gap:10px;height:30px}
.ticks li:before{content:"";width:14px;height:14px;background:var(--green);border-radius:2px;flex:none}
.realtime .join{left:639px;top:361px;width:160px;height:38px;background:var(--blue);color:#fff;font-size:12px}

/* pricing */
.pricing{position:absolute;left:0;top:2264px;width:1200px;height:658px;background:#fff}
.pricing .sec-title{top:50px;font-size:28px}
.pricing .sec-title em{font-style:normal;color:var(--green)}
.plan{position:absolute;background:var(--grey);text-align:center}
.plan .head{height:72px;background:var(--blue);color:#fff;font-size:19px;font-weight:500;display:flex;align-items:center;justify-content:center}
.plan .price{background:#fff;height:112px;padding-top:20px;color:var(--ink)}
.plan .price b{font-size:40px;font-weight:700}
.plan .price sup{font-size:18px;font-weight:700}
.plan .price small{font-size:14px;font-weight:700}
.plan .price p{font-size:12px;color:var(--text);margin-top:2px}
.plan .info{padding:24px 30px 0;font-size:13px;line-height:1.5}
.plan .info strong{display:block;color:var(--ink)}
.pill{position:absolute;height:44px;border-radius:22px;background:var(--blue);color:#fff;font-size:13px;font-weight:700;display:flex;align-items:center;padding-left:32px;gap:16px}
.pill i{width:34px;height:34px;border-radius:50%;background:#fff;display:flex;align-items:center;justify-content:center}
.plan.featured{background:#fff;box-shadow:0 4px 18px rgba(0,0,0,.2);z-index:2}
.plan.featured .head{background:var(--green);height:75px}
.plan.featured .pill{background:var(--green)}

/* features */
.features{position:absolute;left:0;top:2922px;width:1200px;height:495px;background:linear-gradient(90deg,#9a9a9a,#d0d0d0)}
.woman{left:708px;top:0;width:492px;height:495px;background:linear-gradient(120deg,#e8e8e8 0%,#bdbdbd 50%,#8c8c8c 100%)}
.feat-panel{position:absolute;left:161px;top:0;width:547px;height:495px;background:rgba(243,243,243,.95)}
.feat-panel h3{position:absolute;left:0;top:42px;width:547px;text-align:center;font-size:33px;font-weight:700;color:var(--green)}
.feat-panel h4{position:absolute;left:0;top:82px;width:547px;text-align:center;font-size:25px;font-weight:300;color:var(--ink)}
.feat{position:absolute;width:170px;text-align:center}
.feat .ico{width:46px;height:46px;margin:0 auto;border-radius:50%;background:#3e4246;display:flex;align-items:center;justify-content:center}
.feat h5{margin-top:10px;font-size:12px;font-weight:700;color:var(--ink)}
.feat p{margin-top:6px;font-size:10px;line-height:1.45}
.feat-panel .more{left:205px;top:430px;width:136px;height:36px;border:2px solid #777;color:var(--ink);font-size:12px;gap:8px;background:#fff}

/* consultation */
.consult{position:absolute;left:0;top:3417px;width:1200px;height:353px;background:linear-gradient(90deg,#5aa634,#64b23d)}
.video{position:absolute;left:161px;top:41px;width:422px;height:264px;background:#fff;padding:7px}
.video .still{position:relative;width:100%;height:100%;background:linear-gradient(135deg,#c9d4dc 0%,#8aa0b3 50%,#d9dde1 100%)}
.video .play{position:absolute;left:181px;top:95px;width:60px;height:60px;border-radius:50%;background:rgba(255,255,255,.85);display:flex;align-items:center;justify-content:center}
.consult .txt{position:absolute;left:620px;top:66px;width:520px;text-align:center;color:#fff}
.consult h3{font-size:29px;font-weight:700}
.consult .sub{margin-top:10px;font-size:23px;font-weight:300;line-height:1.35}
.consult .note{margin-top:8px;font-size:12px}
.consult .call{left:758px;top:230px;width:166px;height:38px;background:#fff;color:var(--ink);font-size:13px;font-weight:700;gap:8px}

/* footer */
.footer{position:absolute;left:0;top:3770px;width:1200px;height:397px;background:var(--footer);color:var(--footer-text);font-size:11px}
.footer .logo{left:161px;top:40px;font-size:24px}
.footer .logo .dot{width:26px;height:26px}
.footer .about{position:absolute;left:161px;top:88px;width:280px;line-height:1.6}
.footer .about p+p{margin-top:10px}
.fcol{position:absolute;top:42px}
.fcol h6{font-size:15px;font-weight:400;color:#e6e6e6;margin-bottom:18px}
.fcol li{list-style:none;margin-bottom:11px;display:flex;align-items:center;gap:8px}
.fcol li:before{content:"›";color:var(--footer-text)}
.fcol.plain li:before{content:none}
.social{display:flex;gap:8px;margin-top:6px}
.social span{width:26px;height:26px;border-radius:50%;border:1px solid #666}
.news h6,.trust h6{font-size:15px;font-weight:400;color:#e6e6e6}
.news{position:absolute;left:161px;top:262px}
.news .form{display:flex;margin-top:20px}
.news .field{width:310px;height:34px;background:#f1f1f1;color:#999;padding:10px 14px;font-size:11px}
.news .sign{width:100px;height:34px;margin-left:10px;background:var(--blue);color:#fff;font-size:14px;display:flex;align-items:center;justify-content:center}
.trust{position:absolute;left:694px;top:262px}
.badges{display:flex;align-items:center;gap:14px;margin-top:18px}
.b-round{width:56px;height:56px;border-radius:50%;background:#c9302c}
.b-gold{width:52px;height:52px;border-radius:50%;background:#c9a13b}
.b-rect{width:140px;height:46px;border-radius:3px;background:#f4f4f4}
</style>
</head>
<body>

<header class="hero">
  <div class="photo hero-photo" role="img" aria-label="Photo of a smiling senior couple working together on a laptop"></div>
  <div class="topbar">
    <span class="abs email">info@brightdesk.com</span>
    <span class="abs right"><span>United States ▾</span><span>Login</span></span>
  </div>
  <nav class="nav">
    <div class="logo"><span class="dot"></span>brightdesk</div>
    <div class="nav-links"><span>HOME</span><span>ABOUT US</span><span>SERVICES</span><span>CONTACT US</span></div>
    <div class="nav-phone">
      <svg width="20" height="20" viewBox="0 0 24 24"><path fill="#fff" d="M6.6 10.8a15.1 15.1 0 0 0 6.6 6.6l2.2-2.2c.3-.3.7-.4 1-.2 1.1.4 2.3.6 3.6.6.6 0 1 .4 1 1V20c0 .6-.4 1-1 1A17 17 0 0 1 3 4c0-.6.4-1 1-1h3.5c.6 0 1 .4 1 1 0 1.3.2 2.5.6 3.6.1.3 0 .7-.2 1z"/></svg>
      (888) 555-0142
    </div>
  </nav>
  <h1>Dedicated Support</h1>
  <h2>Anytime.Anywhere.</h2>
  <ul class="hero-list">
    <li><span><b>Real-Time</b> Optimization</span></li>
    <li><span><b>Free</b> Diagnostic</span></li>
    <li><span><b>Unlimited</b> Cloud Backup</span></li>
    <li><span><b>Leading</b> Security Software</span></li>
  </ul>
  <a class="btn cta">Get FREE PC help now</a>
</header>

<section class="member">
  <div class="icon">
    <svg width="74" height="52" viewBox="0 0 74 52"><circle cx="20" cy="15" r="8" fill="#fff" opacity=".8"/><circle cx="54" cy="15" r="8" fill="#fff" opacity=".8"/><circle cx="37" cy="13" r="11" fill="#fff"/><path d="M6 46c0-10 6-16 14-16s10 4 10 4H6z" fill="#fff" opacity=".8"/><path d="M68 46c0-10-6-16-14-16s-10 4-10 4h24z" fill="#fff" opacity=".8"/><path d="M18 50c0-14 8-22 19-22s19 8 19 22z" fill="#fff"/></svg>
  </div>
  <h3>BECOME A MEMBER TODAY!</h3>
  <p>Join members in Europe, the Americas and Asia for fast, friendly computer help.</p>
  <a class="btn go">GET IT NOW <svg width="14" height="14" viewBox="0 0 14 14"><circle cx="7" cy="7" r="7" fill="#fff"/><path d="M5.5 4l3 3-3 3" stroke="#5aa634" stroke-width="1.6" fill="none"/></svg></a>
</section>

<section class="how">
  <h2 class="sec-title">HOW IT WORKS</h2>
  <p class="lead">Wherever you live, in Europe, North or South America or Asia, getting help is simple: tell us what is wrong, let a certified technician connect securely, and relax while we fix it.</p>
  <div class="step" style="left:157px">
    <div class="ring"><svg width="44" height="40" viewBox="0 0 44 40"><rect x="4" y="4" width="36" height="24" rx="2" fill="none" stroke="#2a2f35" stroke-width="2.5"/><path d="M14 36h16M22 28v8" stroke="#2a2f35" stroke-width="2.5"/><path d="M12 20l6-6 5 4 8-8" stroke="#1e90ec" stroke-width="2.5" fill="none"/></svg></div>
    <h4>FREE Diagnostic</h4>
    <p>We run a complete free check of your computer to find what slows it down, then explain the results in plain words.</p>
  </div>
  <div class="step" style="left:465px">
    <div class="ring"><svg width="44" height="40" viewBox="0 0 44 40"><rect x="4" y="4" width="36" height="24" rx="2" fill="none" stroke="#2a2f35" stroke-width="2.5"/><path d="M14 36h16M22 28v8" stroke="#2a2f35" stroke-width="2.5"/><circle cx="22" cy="16" r="6" fill="none" stroke="#1e90ec" stroke-width="2.5"/></svg></div>
    <h4>Get Fixed</h4>
    <p>A friendly expert connects remotely and repairs errors, viruses and slow startups while you watch every single step.</p>
  </div>
  <div class="step" style="left:773px">
    <div class="ring"><svg width="44" height="40" viewBox="0 0 44 40"><rect x="4" y="4" width="36" height="24" rx="2" fill="none" stroke="#2a2f35" stroke-width="2.5"/><path d="M14 36h16M22 28v8" stroke="#2a2f35" stroke-width="2.5"/><path d="M15 21a5 5 0 0 1 1-10 7 7 0 0 1 13 2 4 4 0 0 1 0 8z" fill="none" stroke="#1e90ec" stroke-width="2.5"/></svg></div>
    <h4>Backup your information!</h4>
    <p>Your photos, files and documents are copied safely to secure cloud storage so nothing important is ever lost again.</p>
  </div>
  <a class="btn more">READ MORE <svg width="14" height="14" viewBox="0 0 14 14"><circle cx="7" cy="7" r="7" fill="#2a2f35"/><path d="M5.5 4l3 3-3 3" stroke="#fff" stroke-width="1.6" fill="none"/></svg></a>
</section>

<section class="band">
  <h3>Computer Repair and IT Support Services</h3>
  <p>We're a 24/7, Cost Efficient Tech Repair Service for You, Worldwide</p>
  <a class="btn contact">CONTACT US</a>
</section>

<section class="products">
  <h2 class="sec-title">Our Products</h2>
  <div class="product" style="left:161px">
    <div class="shot" role="img" aria-label="Photo of a laptop screen showing a protected status" style="background:linear-gradient(160deg,#2f7f3c 0%,#4fa75a 45%,#b9dcb2 100%)"></div>
    <p class="cap">Total PC Protection, 1 Year</p><p class="price">$61.19</p>
    <div class="row"><span class="view">view more</span><span class="cart">Add to cart</span></div>
  </div>
  <div class="product" style="left:386px">
    <div class="shot" role="img" aria-label="Photo of an online security book with a padlock" style="background:linear-gradient(160deg,#f2f2f2 0%,#c4c4c4 50%,#6f6f6f 100%)"></div>
    <p class="cap">Online Security Suite, 1 Year</p><p class="price">$61.19</p>
    <div class="row"><span class="view">view more</span><span class="cart">Add to cart</span></div>
  </div>
  <div class="product" style="left:608px">
    <div class="shot" role="img" aria-label="Illustration of data privacy with a shield and laptop" style="background:linear-gradient(160deg,#e4f1f7 0%,#a9cfe2 50%,#6ea7c4 100%)"></div>
    <p class="cap">Data Privacy Guard, 1 Year</p><p class="price">$61.19</p>
    <div class="row"><span class="view">view more</span><span class="cart">Add to cart</span></div>
  </div>
  <div class="product" style="left:833px">
    <div class="shot" role="img" aria-label="Illustration of a blue digital padlock" style="background:linear-gradient(160deg,#174f8f 0%,#2f7fcf 50%,#9cc8ef 100%)"></div>
    <p class="cap">Secure Cloud Backup, 1 Year</p><p class="price">$61.19</p>
    <div class="row"><span class="view">view more</span><span class="cart">Add to cart</span></div>
  </div>
</section>

<section class="realtime">
  <div class="photo family" role="img" aria-label="Photo of a smiling family gathered around a laptop"></div>
  <h3 class="t1">REAL-TIME</h3>
  <p class="t2">SUPPORT FEATURES AND</p>
  <p class="t3">BENEFITS</p>
  <ul class="ticks">
    <li>24/7 Real-Time Technician Support</li>
    <li>The best Security Software in the market</li>
    <li>Regular tune-ups and optimization</li>
    <li>Setup and Installation Included</li>
  </ul>
  <a class="btn join">BECOME A MEMBER</a>
</section>

<section class="pricing">
  <h2 class="sec-title">MEMBERSHIP PRICING AND <em>PLANS</em></h2>
  <div class="plan" style="left:161px;top:156px;width:283px;height:419px">
    <div class="head">PREMIUM</div>
    <div class="price"><sup>$</sup><b>19.99</b><small>/MONTHLY</small><p>($249-$300 setup fee)</p></div>
    <div class="info">Regular 90-Day Optimization<strong>Unlimited 24/7 Tier 3 Technician Support</strong></div>
    <a class="pill" style="left:56px;top:337px;width:170px">LEARN MORE <i><svg width="12" height="12" viewBox="0 0 12 12"><path d="M4 2l4 4-4 4" stroke="#1e90ec" stroke-width="2" fill="none"/></svg></i></a>
  </div>
  <div class="plan featured" style="left:444px;top:131px;width:312px;height:472px">
    <div class="head">PREMIUM PLUS</div>
    <div class="price"><sup>$</sup><b>29.99</b><small>/MONTHLY</small><p>($249-$300 setup fee)</p></div>
    <div class="info" style="background:var(--grey);height:90px">Regular 90-Day Optimization<strong>Unlimited 24/7 Tier 3 Technician Support</strong></div>
    <a class="pill" style="left:53px;top:362px;width:206px;height:54px;border-radius:27px">LEARN MORE <i><svg width="12" height="12" viewBox="0 0 12 12"><path d="M4 2l4 4-4 4" stroke="#5aa634" stroke-width="2" fill="none"/></svg></i></a>
  </div>
  <div class="plan" style="left:756px;top:156px;width:283px;height:419px">
    <div class="head">PLATINUM</div>
    <div class="price"><sup>$</sup><b>19.99</b><small>/MONTHLY</small><p>($249-$300 setup fee)</p></div>
    <div class="info">Regular 90-Day Optimization<strong>Unlimited 24/7 Tier 3 Technician Support</strong></div>
    <a class="pill" style="left:56px;top:337px;width:170px">LEARN MORE <i><svg width="12" height="12" viewBox="0 0 12 12"><path d="M4 2l4 4-4 4" stroke="#1e90ec" stroke-width="2" fill="none"/></svg></i></a>
  </div>
</section>

<section class="features">
  <div class="photo woman" role="img" aria-label="Black and white photo of a woman holding a mug at her laptop"></div>
  <div class="feat-panel">
    <h3>ALL THE BEST FEATURES</h3>
    <h4>AT THE BEST PRICE!</h4>
    <div class="feat" style="left:10px;top:132px"><div class="ico"><svg width="20" height="20" viewBox="0 0 20 20"><rect x="2" y="3" width="16" height="11" fill="none" stroke="#fff" stroke-width="2"/><path d="M6 17h8" stroke="#fff" stroke-width="2"/></svg></div><h5>AD BLOCKER</h5><p>Avoid unwanted pop-ups with our newest ad blocking tools for a calmer web.</p></div>
    <div class="feat" style="left:190px;top:132px"><div class="ico"><svg width="20" height="20" viewBox="0 0 20 20"><rect x="3" y="3" width="14" height="14" fill="none" stroke="#fff" stroke-width="2"/><path d="M7 10h6M10 7v6" stroke="#fff" stroke-width="2"/></svg></div><h5>REGULAR TUNE-UPS</h5><p>Get a regular tune-up and optimization every 90 days to stay fast.</p></div>
    <div class="feat" style="left:368px;top:132px"><div class="ico"><svg width="20" height="20" viewBox="0 0 20 20"><rect x="2" y="3" width="16" height="11" fill="none" stroke="#fff" stroke-width="2"/><path d="M5 11l3-3 3 2 4-4" stroke="#fff" stroke-width="2" fill="none"/></svg></div><h5>SYSTEM REPORTS</h5><p>Stay up to date with clear real-time system reporting each month.</p></div>
    <div class="feat" style="left:10px;top:276px"><div class="ico"><svg width="20" height="20" viewBox="0 0 20 20"><rect x="2" y="4" width="11" height="9" fill="none" stroke="#fff" stroke-width="2"/><rect x="13" y="7" width="5" height="9" fill="none" stroke="#fff" stroke-width="2"/></svg></div><h5>MULTIPLE DEVICES</h5><p>Get support for up to five devices. Ask about our family plans.</p></div>
    <div class="feat" style="left:190px;top:276px"><div class="ico"><svg width="20" height="20" viewBox="0 0 20 20"><rect x="6" y="2" width="8" height="16" rx="1" fill="none" stroke="#fff" stroke-width="2"/></svg></div><h5>MOBILE SECURITY</h5><p>Keep phones and tablets safe with guarded browsing every day.</p></div>
    <div class="feat" style="left:368px;top:276px"><div class="ico"><svg width="20" height="20" viewBox="0 0 20 20"><path d="M5 15a4 4 0 0 1 1-8 5 5 0 0 1 9 2 3 3 0 0 1 0 6z" fill="none" stroke="#fff" stroke-width="2"/></svg></div><h5>CLOUD BACKUP</h5><p>Keep your data safe. Ask about our plans for unlimited cloud backup.</p></div>
    <a class="btn more">VIEW MORE <svg width="14" height="14" viewBox="0 0 14 14"><circle cx="7" cy="7" r="7" fill="#2a2f35"/><path d="M5.5 4l3 3-3 3" stroke="#fff" stroke-width="1.6" fill="none"/></svg></a>
  </div>
</section>

<section class="consult">
  <div class="video">
    <div class="still" role="img" aria-label="Video still of a smiling older man at his computer">
      <div class="play"><svg width="22" height="24" viewBox="0 0 22 24"><path d="M3 2l17 10L3 22z" fill="#5aa634"/></svg></div>
    </div>
  </div>
  <div class="txt">
    <h3>GET A 30-MINUTE ONE-ON-ONE</h3>
    <p class="sub">FREE CONSULTATION WITH ONE<br>OF OUR EXPERTS! *</p>
    <p class="note">*Limited period offer</p>
  </div>
  <a class="btn call"><svg width="14" height="14" viewBox="0 0 24 24"><path fill="#2a2f35" d="M6.6 10.8a15.1 15.1 0 0 0 6.6 6.6l2.2-2.2c.3-.3.7-.4 1-.2 1.1.4 2.3.6 3.6.6.6 0 1 .4 1 1V20c0 .6-.4 1-1 1A17 17 0 0 1 3 4c0-.6.4-1 1-1h3.5c.6 0 1 .4 1 1 0 1.3.2 2.5.6 3.6.1.3 0 .7-.2 1z"/></svg>CALL US TODAY</a>
</section>

<footer class="footer">
  <div class="logo"><span class="dot"></span>brightdesk</div>
  <div class="about">
    <p>We are a global team of technicians working round the clock across Europe, the Americas and Asia to make sure your PC runs perfectly and stays healthy.</p>
    <p>You can get in touch with us at any time of the day, any day of the week. We offer support through phone and online chat.</p>
  </div>
  <div class="fcol" style="left:486px">
    <h6>Quick Links</h6>
    <ul><li>Home</li><li>About Us</li><li>Services</li><li>Contact Us</li><li>FAQs</li></ul>
  </div>
  <div class="fcol plain" style="left:694px">
    <h6>Our Support</h6>
    <ul><li>Contact us</li><li>support@brightdesk.com</li><li>+1 (888) 555-0142</li></ul>
    <div class="social"><span></span><span></span><span></span><span></span></div>
  </div>
  <div class="fcol" style="left:939px">
    <h6>Plans</h6>
    <ul><li>Premium Plan</li><li>Premium Plus Plan</li><li>Platinum Plan</li></ul>
  </div>
  <div class="news">
    <h6>Newsletter Signup</h6>
    <div class="form"><span class="field">Enter your email</span><span class="sign">Sign up</span></div>
  </div>
  <div class="trust">
    <h6>Trusted By</h6>
    <div class="badges"><span class="b-round"></span><span class="b-gold"></span><span class="b-rect"></span></div>
  </div>
</footer>

</body>
</html>
```